seeking a modern Business Card design for Roof Plumbering Business

wexcombe roof plumbing is a local metal re-roof and new construction specialist. We are seeking a modern business card to assist with networking within the industry. Our services are predominantly the installation of metal roofs on new houses, however we also do re-roofs when an existing roof needs replacing. We service both residential and commercial properties. Please include the below details on the card:
Name: Owen Wexcombe
Phone: 0471 385 962
Email: owenwexcomberoofing@mailnest.example

Residential & Commercial
Re-roof & New Construction
Fully Insured

I have uploaded our business logo, which we think would suit a black background. Please use all lower case for business name.
Cheers
Updates

Hey Guys, As requested I've uploaded a Pdf version of my logo. Hopefully this help. Thanks

Industry/Entity Type

Business

Contact Information for Business Card

Name: Owen Wexcombe
Phone: 0471 385 962

Residential & Commercial
Fully Insured

Font styles to use
Serif
Sans Serif

Requirements
Must have
• Name must be all lower case "wexcombe roof plumbing"
Nice to have
• Stick with Logo Colours

```html
<!DOCTYPE html>
<html lang="en">
<head>
<meta charset="utf-8">
<title>wexcombe roof plumbing – business card</title>
<link href="https://fonts.googleapis.com/css2?family=Arimo:wght@400&family=Tinos:wght@400&display=swap" rel="stylesheet">
<style>
  :root {
    --page-bg: #e8e5e0;
    --panel-dark: #2c2c2d;
    --panel-dark-edge: #3b3b3c;
    --card-light: #dddbd7;
    --card-light-edge: #cfccc7;
    --teal: #33a3a3;
    --name-teal: #2c9a8f;
    --ink: #151515;
  }
  * { box-sizing: border-box; margin: 0; padding: 0; }
  html, body {
    width: 1200px;
    height: 970px;
    overflow: hidden;
    background: var(--page-bg);
  }
  .business-card {
    position: absolute;
    left: 100px;
    top: 186px;
    width: 1000px;
    height: 598px;
    display: flex;
    box-shadow: 0 10px 30px rgba(0,0,0,0.18);
  }
  .brand-panel {
    position: relative;
    width: 462px;
    height: 100%;
    background: radial-gradient(ellipse at 50% 35%, var(--panel-dark-edge), var(--panel-dark) 75%);
  }
  .brand-name {
    position: absolute;
    left: 0;
    right: 0;
    top: 290px;
    display: flex;
    align-items: center;
    justify-content: center;
    gap: 14px;
    font-family: "Arimo", Arial, sans-serif;
    font-weight: 400;
    font-size: 30px;
    line-height: 1;
    color: var(--teal);
  }
  .brand-mark {
    width: 28px;
    height: 28px;
    flex: none;
    background: var(--teal);
  }
  .details-panel {
    position: relative;
    flex: 1;
    height: 100%;
    background: linear-gradient(160deg, var(--card-light), var(--card-light-edge));
    text-align: right;
    font-family: "Arimo", Arial, sans-serif;
    color: var(--ink);
  }
  .owner-name {
    position: absolute;
    right: 40px;
    top: 98px;
    font-family: "Tinos", "Times New Roman", serif;
    font-weight: 400;
    font-size: 44px;
    color: var(--name-teal);
    white-space: nowrap;
  }
  .contact-list {
    position: absolute;
    right: 28px;
    top: 224px;
    list-style: none;
  }
  .contact-item {
    display: flex;
    align-items: center;
    justify-content: flex-end;
    height: 36px;
    margin-bottom: 7px;
    font-size: 26px;
    white-space: nowrap;
  }
  .contact-item.email { font-size: 22px; }
  .contact-icon {
    width: 35px;
    height: 35px;
    margin-left: 14px;
    flex: none;
  }
  .service-list {
    position: absolute;
    right: 40px;
    top: 362px;
    list-style: none;
    font-size: 30px;
    line-height: 46px;
    white-space: nowrap;
  }
</style>
</head>
<body>
  <div class="business-card">
    <section class="brand-panel">
      <div class="brand-name">
        <span class="brand-mark" aria-hidden="true"></span>
        <span>wexcombe roof plumbing</span>
      </div>
    </section>
    <section class="details-panel">
      <h1 class="owner-name">Owen Wexcombe</h1>
      <ul class="contact-list">
        <li class="contact-item phone">
          <span>0471 385 962</span>
          <svg class="contact-icon" viewBox="0 0 35 35" aria-hidden="true">
            <rect width="35" height="35" fill="var(--teal)"/>
            <path d="M8 14 Q17.5 7 27 14 L25 17 L21 15 L21 13 Q17.5 11.5 14 13 L14 15 L10 17 Z" fill="none" stroke="#fff" stroke-width="1.6"/>
            <rect x="10" y="18" width="15" height="10" rx="1.5" fill="none" stroke="#fff" stroke-width="1.6"/>
            <circle cx="17.5" cy="23" r="2.5" fill="none" stroke="#fff" stroke-width="1.4"/>
          </svg>
        </li>
        <li class="contact-item email">
          <span>owenwexcomberoofing@mailnest.example</span>
          <svg class="contact-icon" viewBox="0 0 35 35" aria-hidden="true">
            <rect width="35" height="35" fill="var(--teal)"/>
            <rect x="7" y="10" width="21" height="15" fill="none" stroke="#fff" stroke-width="1.6"/>
            <path d="M7 10 L17.5 19 L28 10 M7 25 L14.5 17 M28 25 L20.5 17" fill="none" stroke="#fff" stroke-width="1.6"/>
          </svg>
        </li>
      </ul>
      <ul class="service-list">
        <li>Residential &amp; Commercial</li>
        <li>Re-roof &amp; New Construction</li>
        <li>Fully Insured</li>
      </ul>
    </section>
  </div>
</body>
</html>
```